Cat-products company needs smart, yet endearing, business card

We need a business card design for a new, but up-and-running, business based in Honolulu, Hawaii. The business is Purrlane Nest Co. Our first product is the most environmentally-friendly cat grass kit ever seen on the planet. Future products, currently in the R&D phase, will include a variety of exciting cat scratchers. We also do consulting work to help apartment-dwellers make their home more cat-friendly and, in the future, plan on doing full, custom installs of structure to create high walkways for cats.

Target Market(s)

Middle-aged, apartment-dwelling, middle-class workers who own 1 or more cats and who dote on them.

Industry/Entity Type

Pet Care

Contact Information for Business Card

A striking, professional, yet warm and friendly design is what we're after.

Font styles to use
Serif
Sans Serif
Other font styles liked:
• Comfortaa

Colors

Designer to choose colors to be used in the design.

Requirements
Must have
• The company logo: (see attachment)
• The company name: Purrlane Nest Co
• The web address: www.purrlanenestco.example
• Email: support@purrlanenestco.example
• Phone: +1 (808) 555 0172
• Update (Fri Jun 30 3017 7:45pm Hawaii Time) I would like, is possible, uploaded picture of the cat grass kit on the back of the card with some text along the lines of: Purrlane Nest Co - Where The Freshest Kitty Sprouts Begin
Nice to have
• A cat picture, cartoon, real or silhouette that illustrates cats in action and/or relaxing; ie using the apartment space to live, play and relax in and being well-contented.
• Most of the website is done in the font: Comfortaa. It might be nice to continue using this for brand consistency.
Should not have
• Hard-to-read fonts.

```html
<!DOCTYPE html>
<html lang="en">
<head>
<meta charset="utf-8">
<title>Purrlane Nest Co – Business Card</title>
<link href="https://fonts.googleapis.com/css2?family=Open+Sans:wght@400;600;700&display=swap" rel="stylesheet">
<style>
  :root {
    --backdrop: #575757;
    --card-white: #ffffff;
    --cocoa: #5a3530;
    --amber: #fdb515;
    --ink: #222222;
  }
  * { margin: 0; padding: 0; box-sizing: border-box; }
  html, body { width: 1200px; height: 900px; overflow: hidden; }
  body {
    background: var(--backdrop);
    font-family: "Open Sans", Arial, sans-serif;
    position: relative;
  }
  .card-shapes { position: absolute; left: 0; top: 0; }
  .front-text { position: absolute; left: 443px; top: 284px; color: var(--ink); }
  .holder-name {
    color: var(--amber);
    font-size: 15px;
    font-weight: 400;
    letter-spacing: 0.2px;
    text-transform: uppercase;
    line-height: 20px;
  }
  .holder-role { font-size: 12px; line-height: 16px; }
  .contact-list { list-style: none; margin-top: 22px; }
  .contact-list li {
    display: flex; align-items: center; gap: 6px;
    font-size: 12px; line-height: 16px;
  }
  .contact-list svg { width: 9px; height: 9px; fill: var(--amber); flex: none; }
  .brand-front {
    position: absolute; left: 650px; top: 212px; width: 140px;
    display: flex; flex-direction: column; align-items: center; gap: 10px;
  }
  .brand-square { width: 46px; height: 46px; background: var(--cocoa); }
  .brand-name-front {
    color: var(--amber);
    font-weight: 700;
    font-size: 24px;
    line-height: 26px;
    text-align: center;
  }
  .brand-back {
    position: absolute; left: 520px; top: 600px; width: 200px;
    color: var(--card-white);
    font-weight: 700;
    font-size: 28px;
    line-height: 32px;
    text-align: center;
  }
</style>
</head>
<body>
  <svg class="card-shapes" width="1200" height="900" viewBox="0 0 1200 900" aria-hidden="true">
    <defs>
      <filter id="card-shadow" x="-10%" y="-10%" width="130%" height="130%">
        <feDropShadow dx="2" dy="3" stdDeviation="2.5" flood-color="#000" flood-opacity="0.45"/>
      </filter>
    </defs>
    <polygon class="card-front" filter="url(#card-shadow)" fill="var(--card-white)"
      points="420,145 722,145 858,275 820,277 820,415 420,415"/>
    <polygon class="card-back" filter="url(#card-shadow)" fill="var(--cocoa)"
      points="540,496 842,496 842,768 442,768 442,630 403,628"/>
  </svg>

  <div class="front-text">
    <p class="holder-name">Marcus Kealoha</p>
    <p class="holder-role">Managing Director</p>
    <ul class="contact-list">
      <li>
        <svg viewBox="0 0 10 10"><path d="M2 0.5 L3.8 2.6 L2.9 3.8 Q4 6 6.2 7.1 L7.4 6.2 L9.5 8 L8.3 9.5 Q1 8 0.5 1.7 Z"/></svg>
        +1 (808) 555 0172
      </li>
      <li>
        <svg viewBox="0 0 10 10"><path d="M0 2 H10 V8.5 H0 Z M0.6 2.4 L5 5.6 L9.4 2.4" stroke="#fff" stroke-width="0.8"/></svg>
        support@purrlanenestco.example
      </li>
      <li>
        <svg viewBox="0 0 10 10"><circle cx="5" cy="5" r="4.8"/><path d="M2.5 3 Q4 4 3.5 5.5 Q5 6 4.5 8 M6 2 Q7 3.5 8.5 3.5" stroke="#fff" stroke-width="0.8" fill="none"/></svg>
        www.purrlanenestco.example
      </li>
    </ul>
  </div>

  <div class="brand-front">
    <div class="brand-square"></div>
    <p class="brand-name-front">Purrlane Nest Co</p>
  </div>

  <p class="brand-back">Purrlane Nest Co</p>
</body>
</html>
```